Real Estate Company needs Stationary.
Business Cards, Letterhead, Envelope Stationary etc...
Real Estate Company needs Stationary. -
Creative Brief
Professional
Tomas Velbrik
Broker
3871 W. Marrowfield Ave., Suite K-214 Marrowfield TX, 75318
1 (866) 514-VKOR (5867)
tomas@vkorhomesllc.example
www.vkorhomesllc.example
We are a real estate company looking for a slick contemporary design. Use logo in the design. Use logo colors if desired. Would like Business cards, Letterhead, and Envelope. I would like all the stationary items to carry the same theme my logo protrays. Email me with questions.
I would like the logo on back, and open to any other sugestions.

```html
<!DOCTYPE html>
<html lang="en">
<head>
<meta charset="utf-8">
<title>vKorHomes Stationery</title>
<link href="https://fonts.googleapis.com/css2?family=Open+Sans:wght@400;600;700&display=swap" rel="stylesheet">
<style>
  :root {
    --backdrop: #6a4227;
    --paper: #ffffff;
    --brand-blue: #1a6cb5;
    --brand-blue-dark: #0f4f8f;
    --brand-blue-light: #3f8fd4;
    --brand-green: #5aab34;
    --ink: #2d3440;
    --ink-soft: #6a717c;
    --card-grey: #d9dadc;
  }
  * { margin: 0; padding: 0; box-sizing: border-box; }
  html, body { width: 1200px; height: 673px; overflow: hidden; }
  body {
    background: var(--backdrop);
    font-family: "Open Sans", Arial, sans-serif;
    color: var(--ink);
    position: relative;
  }
  .piece {
    position: absolute;
    background: var(--paper);
    overflow: hidden;
    box-shadow: 0 3px 10px rgba(0,0,0,.35);
  }
  .piece svg.wave { position: absolute; inset: 0; width: 100%; height: 100%; }
  .brand {
    position: absolute;
    display: flex;
    align-items: center;
    gap: 6px;
    font-weight: 700;
    color: var(--brand-blue);
    white-space: nowrap;
  }
  .brand .mark { background: var(--brand-green); display: block; }
  .contact { position: absolute; color: #fff; line-height: 1.35; }

  /* business card front */
  .card-front { left: 38px; top: 132px; width: 142px; height: 89px; }
  .card-front .brand { left: 8px; top: 9px; font-size: 9px; gap: 3px; }
  .card-front .brand .mark { width: 7px; height: 7px; }
  .card-front .holder { position: absolute; right: 8px; top: 9px; font-size: 5px; line-height: 1.3; text-align: left; }
  .card-front .holder strong { display: block; font-weight: 700; }
  .card-front .contact { font-size: 3.2px; }
  .card-front .contact.left { left: 7px; bottom: 6px; }
  .card-front .contact.right { right: 7px; bottom: 6px; }

  /* business card back */
  .card-back {
    left: 38px; top: 235px; width: 142px; height: 89px;
    background: radial-gradient(ellipse at center, #f4f4f5 0%, var(--card-grey) 75%);
  }
  .card-back .brand { left: 0; right: 0; top: 30px; justify-content: center; font-size: 12px; gap: 4px; }
  .card-back .brand .mark { width: 9px; height: 9px; }
  .card-back .web { position: absolute; left: 0; right: 0; top: 50px; text-align: center; font-size: 4.5px; color: var(--brand-blue-dark); }

  /* letterhead */
  .letterhead { left: 235px; top: 31px; width: 432px; height: 622px; }
  .letterhead .brand { left: 34px; top: 70px; font-size: 26px; gap: 8px; }
  .letterhead .brand .mark { width: 20px; height: 20px; }
  .letterhead .contact { font-size: 8.5px; }
  .letterhead .contact.left { left: 14px; bottom: 14px; }
  .letterhead .contact.right { left: 282px; bottom: 10px; }

  /* envelope front */
  .envelope-front { left: 684px; top: 84px; width: 463px; height: 240px; }
  .envelope-front .brand { left: 36px; top: 66px; font-size: 21px; gap: 7px; }
  .envelope-front .brand .mark { width: 16px; height: 16px; }
  .envelope-front .contact { font-size: 8px; }
  .envelope-front .contact.left { left: 14px; bottom: 50px; }
  .envelope-front .contact.right { left: 318px; bottom: 26px; }

  /* envelope back */
  .envelope-back { left: 684px; top: 348px; width: 463px; height: 252px; }
  .envelope-back .brand { left: 0; right: 0; top: 64px; justify-content: center; font-size: 18px; }
  .envelope-back .brand .mark { width: 14px; height: 14px; }
</style>
</head>
<body>

  <section class="piece card-front" aria-label="Business card front">
    <svg class="wave" viewBox="0 0 142 89" preserveAspectRatio="none" aria-hidden="true">
      <path d="M0 50 Q70 34 142 38 L142 89 L0 89 Z" fill="var(--brand-blue-light)"/>
      <path d="M0 56 Q70 40 142 44 L142 89 L0 89 Z" fill="var(--brand-blue)"/>
      <path d="M0 47 Q70 31 142 35" fill="none" stroke="var(--brand-green)" stroke-width="1.5"/>
    </svg>
    <div class="brand"><span class="mark"></span>vKorHomes</div>
    <div class="holder"><strong>Tomas Velbrik</strong>Broker</div>
    <div class="contact left">3871 W. Marrowfield Ave., Suite K-214<br>Marrowfield TX, 75318</div>
    <div class="contact right">Toll Free: 1 (866) 514-VKOR (5867)<br>tomas@vkorhomesllc.example<br>www.vkorhomesllc.example</div>
  </section>

  <section class="piece card-back" aria-label="Business card back">
    <div class="brand"><span class="mark"></span>vKorHomes</div>
    <div class="web">www.vkorhomesllc.example</div>
  </section>

  <section class="piece letterhead" aria-label="Letterhead">
    <svg class="wave" viewBox="0 0 432 622" preserveAspectRatio="none" aria-hidden="true">
      <path d="M0 548 Q200 508 432 500 L432 622 L0 622 Z" fill="var(--brand-blue-light)"/>
      <path d="M0 558 Q200 518 432 512 L432 622 L0 622 Z" fill="var(--brand-blue)"/>
      <path d="M0 544 Q200 502 432 494" fill="none" stroke="var(--brand-green)" stroke-width="3"/>
    </svg>
    <div class="brand"><span class="mark"></span>vKorHomes</div>
    <div class="contact left">3871 W. Marrowfield Ave., Suite K-214<br>Marrowfield TX, 75318</div>
    <div class="contact right">Toll Free: 1 (866) 514-VKOR (5867)<br>Phone: (817) 624-3190<br>Fax: (817) 624-3195<br>Email: tomas@vkorhomesllc.example<br>www.vkorhomesllc.example</div>
  </section>

  <section class="piece envelope-front" aria-label="Envelope front">
    <svg class="wave" viewBox="0 0 463 240" preserveAspectRatio="none" aria-hidden="true">
      <path d="M0 138 Q230 112 463 106 L463 240 L0 240 Z" fill="var(--brand-blue-light)"/>
      <path d="M0 146 Q230 120 463 116 L463 240 L0 240 Z" fill="var(--brand-blue)"/>
      <path d="M0 134 Q230 106 463 100" fill="none" stroke="var(--brand-green)" stroke-width="3"/>
    </svg>
    <div class="brand"><span class="mark"></span>vKorHomes</div>
    <div class="contact left">3871 W. Marrowfield Ave., Suite K-214<br>Marrowfield TX, 75318</div>
    <div class="contact right">Toll Free: 1 (866) 514-VKOR (5867)<br>Phone: (817) 624-3190<br>Fax: (817) 624-3195<br>Email: tomas@vkorhomesllc.example<br>www.vkorhomesllc.example</div>
  </section>

  <section class="piece envelope-back" aria-label="Envelope back">
    <svg class="wave" viewBox="0 0 463 252" preserveAspectRatio="none" aria-hidden="true">
      <path d="M0 0 L231 138 L463 0" fill="none" stroke="#c9ccd1" stroke-width="1"/>
      <path d="M0 252 L200 120 M463 252 L262 120" fill="none" stroke="#dcdfe3" stroke-width="1"/>
    </svg>
    <div class="brand"><span class="mark"></span>vKorHomes</div>
  </section>

</body>
</html>
```